Tales from Kin Logo Design plus business cards design

We are a start up company that will help seniors write their memoirs...beginning with a few ancestors and their heritage and continuing through their own history...how they would like to be remembered in the next generation. I envision a card with a senior citizen at an older writing desk, writing her memoirs, with a book (maybe standing on top, leaning slightly) that has the words Tales from Kin.com on the back binding. OR maybe a senior couple walking into the sunset with the same book somewhere in the frame. Communicating the relevance of every life being significant to those that come after them...when a genealogy doesn't say enough about the details of ones life. Please note that I am open to the professionals own ideas...I am not locked into my concepts. On the back of the card I would like one or two phrases..."A Genealogy Doesn't Say Enough" and/or "Every life legacy is uniquely significant to the next generation".
Updates

I have added a couple of photos for ideas that may be used if needed.

I have both increased and committed the payment! Thanks for the reminder!

Reason: We increased the payment commitment and added some photo ideas to help.

We want to thank EVERYONE who participated in this contest. There were so many wonderful and VERY professional proposals...making it very challenging to decide on one! We are posting a new contest for a brochure now and hope many of you will participate. May God bless your endeavors.

Target Market(s)

Senior populous & baby boomer generation.

Industry/Entity Type

Business

Logo Text

Tales from Kin ordinary lives...extraordinary legacy

Requirements
Must have
• Relevant info:
Domain name: talesfromkin.com
email: info@talesfromkin.com
phone: 1-855-GAB-TALE toll free
1-717-382-5619 local
name: Doris Whitlock, M.A.
Nice to have
• photo of senior or senior couple....book with our web address on the binding. I attached two photos that could work if cropped and enhanced. Words need to be deleted from the one photo of senior at a writing desk and couple on the beach could use a sunset sky and other people cropped out. Just ideas...don't know if you have better ones or prefer a different idea.

```html
<!DOCTYPE html>
<html lang="en">
<head>
<meta charset="utf-8">
<title>Tales from Kin – Business Card</title>
<link rel="stylesheet" href="https://fonts.googleapis.com/css2?family=Cinzel:wght@400;700&display=swap">
<style>
  :root {
    --stage: #3a3a3a;
    --card-black: #0b0b0b;
    --card-back: #121212;
    --sky-blue: #3cb6ea;
    --sky-blue-light: #8fd8f8;
    --icon-blue: #3aa8dc;
    --text-white: #f2f2f2;
    --logo-grey: #a8a8a8;
    --sunset-orange: #c8552c;
    --sunset-amber: #b27a58;
    --dusk-grey: #3b3f44;
  }
  * { margin: 0; padding: 0; box-sizing: border-box; }
  html, body {
    width: 1200px; height: 750px; overflow: hidden;
    background: var(--stage);
    font-family: "Cinzel", Georgia, serif;
  }
  .card {
    position: absolute; top: 207px;
    width: 523px; height: 299px;
    border-radius: 14px; overflow: hidden;
  }
  .card--front { left: 62px; background: var(--card-black); }
  .card--back { left: 606px; background: var(--card-back); }

  .photo-area {
    position: absolute; left: 220px; top: 0; width: 303px; height: 299px;
    background:
      linear-gradient(to right, var(--card-black) 0%, rgba(11,11,11,0) 35%),
      linear-gradient(to bottom, var(--sunset-orange) 0%, var(--sunset-amber) 30%, var(--dusk-grey) 55%, #2a2724 80%, #1c1a18 100%);
  }
  .brand-name {
    position: absolute; left: 28px; top: 38px;
    font-weight: 700; font-size: 33px; color: var(--sky-blue);
    white-space: nowrap;
  }
  .name-tab {
    position: absolute; left: 0; top: 116px; width: 15px; height: 59px;
    background: var(--sky-blue); border-radius: 0 8px 8px 0;
  }
  .person-name {
    position: absolute; left: 27px; top: 135px;
    font-weight: 700; font-size: 15px; color: var(--sky-blue); letter-spacing: .3px;
  }
  .contact-list {
    position: absolute; left: 27px; top: 190px; list-style: none;
  }
  .contact-list li {
    display: flex; align-items: center; height: 15.5px;
    font-size: 11.5px; color: var(--text-white); letter-spacing: .2px;
  }
  .contact-list svg { width: 12px; height: 12px; margin-right: 10px; fill: var(--icon-blue); }
  .wave { position: absolute; left: 0; bottom: 0; width: 523px; height: 299px; }

  .back-logo {
    position: absolute; left: 0; right: 0; top: 128px; text-align: center;
    font-weight: 700; font-size: 33px; color: var(--logo-grey);
  }
</style>
</head>
<body>
  <section class="card card--front">
    <div class="photo-area" role="img" aria-label="Photo of an elderly couple walking along a beach at sunset"></div>
    <svg class="wave" viewBox="0 0 523 299" aria-hidden="true">
      <defs>
        <linearGradient id="waveBlue" x1="0" x2="1" y1="0" y2="0">
          <stop offset="0" stop-color="#3cb6ea"/>
          <stop offset=".55" stop-color="#8fd8f8"/>
          <stop offset="1" stop-color="#3cb6ea"/>
        </linearGradient>
      </defs>
      <path d="M0 248 C60 262 130 282 220 284 C150 290 60 284 0 272 Z" fill="#5a5a5a"/>
      <path d="M0 270 C120 290 250 270 360 246 C430 232 490 250 523 284 L523 299 L0 299 Z" fill="url(#waveBlue)"/>
    </svg>
    <div class="brand-name">Tales from Kin</div>
    <div class="name-tab"></div>
    <div class="person-name">Doris Whitlock, M.A.</div>
    <ul class="contact-list">
      <li><svg viewBox="0 0 24 24"><path d="M6.6 10.8a15 15 0 0 0 6.6 6.6l2.2-2.2c.3-.3.7-.4 1-.2 1.1.4 2.3.6 3.6.6.6 0 1 .4 1 1V20c0 .6-.4 1-1 1A17 17 0 0 1 3 4c0-.6.4-1 1-1h3.5c.6 0 1 .4 1 1 0 1.3.2 2.5.6 3.6.1.3 0 .7-.2 1z"/></svg>1-855-GAB-TALE toll free</li>
      <li><svg viewBox="0 0 24 24"><path d="M6.6 10.8a15 15 0 0 0 6.6 6.6l2.2-2.2c.3-.3.7-.4 1-.2 1.1.4 2.3.6 3.6.6.6 0 1 .4 1 1V20c0 .6-.4 1-1 1A17 17 0 0 1 3 4c0-.6.4-1 1-1h3.5c.6 0 1 .4 1 1 0 1.3.2 2.5.6 3.6.1.3 0 .7-.2 1z"/></svg>1-717-382-5619 local</li>
      <li><svg viewBox="0 0 24 24"><path d="M2 5h20v14H2z M3.5 6.5 12 13l8.5-6.5" fill="none" stroke="#3aa8dc" stroke-width="2"/></svg>info@talesfromkin.com</li>
      <li><svg viewBox="0 0 24 24"><g fill="none" stroke="#3aa8dc" stroke-width="1.8"><circle cx="12" cy="12" r="9.5"/><ellipse cx="12" cy="12" rx="4" ry="9.5"/><path d="M2.5 12h19M4 7h16M4 17h16"/></g></svg>www.talesfromkin.com</li>
    </ul>
  </section>

  <section class="card card--back">
    <div class="back-logo">Tales from Kin</div>
  </section>
</body>
</html>
```